Podcast Cover Art for Alliance Growth Circle

We need a podcast cover design for a podcast called "Alliance Growth Circle". The podcast is about partnerships in the enterprise software business. The "cover design" is kind of like an album cover and there's a great article here about how to create a stunning Podcast cover art:

https://www.wavelumen.com/blog/10-tips-create-awesome-podcast-artwork

There are also examples in that post linked above.

The Alliance Growth Circle already has some design themes/elements that I'll attach a background image for reference so you can see the typical colors, fonts, etc.

The cover art should include the words "Alliance Growth Circle" and include the names of the two artists:

Derek Halvor
Trevor Lindqvist

It should also include the Alliance Growth Circle logo somewhere. I'll attach that.

I've attached the fonts used for the logo text.

I'll also attach photos of the two artists (2 options to choose from for each). We need your guidance on whether we should include those in some stylized way, or leave them out.

Thanks for the help!

Technical Specifications:

Square Image
3000 x 3000 pixels
Resolution of 72 dpi
PNG or JPEG file types
Colorspace RGB

Colors
0054AA
0677BA
7BADD7
CADEEF
E8F1F8

Requirements
Should not have
• Avoid overused images like microphones and headsets

```html
<!DOCTYPE html>
<html lang="en">
<head>
<meta charset="utf-8">
<title>Alliance Growth Circle – Podcast Cover</title>
<link rel="stylesheet" href="https://fonts.googleapis.com/css2?family=Lexend:wght@300;700;800;900&family=Montserrat:wght@700;800&family=Mrs+Saint+Delafield&display=swap">
<style>
  :root {
    --royal: #0054AA;
    --ocean: #0677BA;
    --sky: #7BADD7;
    --mist: #CADEEF;
    --ice: #E8F1F8;
    --paper: #f4f4f2;
    --ink: #0a0a0a;
    --slate: #2b2b2b;
  }
  * { margin: 0; padding: 0; box-sizing: border-box; }
  html, body { width: 1200px; height: 1200px; overflow: hidden; background: var(--royal); }
  .cover {
    position: relative; width: 1200px; height: 1200px; overflow: hidden;
    background: var(--royal);
    font-family: "Lexend", sans-serif;
  }
  .host-photo { position: absolute; top: 0; width: 1200px; height: 1200px; }
  .host-photo--left {
    left: 0;
    clip-path: polygon(0 0, 230px 0, 255px 120px, 262px 300px, 258px 480px, 300px 560px, 370px 640px, 400px 800px, 410px 1200px, 0 1200px);
    background: linear-gradient(180deg, #9c8577 0%, #c49a86 30%, #b88c79 50%, #8f94a4 58%, #262626 64%, #1b1b1b 100%);
  }
  .host-photo--right {
    left: 0;
    clip-path: polygon(1200px 0, 1000px 0, 960px 130px, 925px 280px, 915px 450px, 890px 600px, 850px 720px, 830px 820px, 840px 1150px, 1200px 1150px);
    background: linear-gradient(180deg, #4a4440 0%, #8e7a70 15%, #b8988a 35%, #a88576 55%, #8e9aa8 70%, #7c8898 100%);
  }
  .paint-band { position: absolute; inset: 0; width: 1200px; height: 1200px; }

  .badge { position: absolute; left: 300px; top: 62px; width: 310px; height: 140px; }
  .badge svg { position: absolute; inset: 0; }
  .badge__text {
    position: absolute; left: 70px; top: 38px; transform: rotate(-24deg);
    color: #fff; font-family: "Montserrat", sans-serif; font-weight: 800; text-align: center; line-height: 1;
  }
  .badge__live { font-size: 30px; letter-spacing: 0.05em; display: block; }
  .badge__podcast { font-size: 19px; letter-spacing: 0.1em; display: block; margin-top: 4px; margin-left: 30px; }

  .title {
    position: absolute; left: 0; right: 0; top: 195px; text-align: center;
    font-weight: 800; font-size: 104px; line-height: 106px; color: var(--ink);
    text-transform: uppercase; letter-spacing: -0.01em;
  }
  .title span { display: block; }
  .title__script {
    position: absolute; left: 650px; top: 440px;
    font-family: "Mrs Saint Delafield", cursive; font-size: 170px; line-height: 1;
    color: var(--ocean);
  }

  .schedule { position: absolute; left: 0; right: 0; top: 712px; text-align: center; color: var(--ink); }
  .schedule__date { font-weight: 800; font-size: 37px; line-height: 44px; padding-left: 10px; }
  .schedule__time { font-weight: 300; font-size: 34px; line-height: 40px; }

  .hosts { position: absolute; left: 0; right: 0; top: 845px; height: 118px; }
  .hosts__divider { position: absolute; left: 599px; top: 0; width: 3px; height: 118px; background: var(--ink); }
  .host-name {
    position: absolute; top: 38px; font-family: "Montserrat", sans-serif; font-weight: 800;
    font-size: 37px; letter-spacing: 0.1em; text-transform: uppercase; white-space: nowrap;
  }
  .host-name--left {
    left: 0; width: 584px; text-align: right;
    background: linear-gradient(90deg, #ffffff 0, #ffffff 352px, var(--ink) 352px, var(--ink) 100%);
    -webkit-background-clip: text; background-clip: text;
    color: transparent;
  }
  .host-name--right { left: 616px; color: var(--ink); }

  .contact { position: absolute; left: 0; right: 0; top: 1042px; text-align: center;
    font-weight: 700; color: var(--slate); }
  .contact__row { display: flex; justify-content: center; align-items: center; gap: 12px; }
  .contact__row--phone { font-size: 29px; height: 48px; }
  .contact__row--stream { font-size: 28px; height: 48px; margin-top: 10px; }
  .contact__number { color: var(--ocean); }
  .icon-ring { width: 44px; height: 44px; border: 4px solid var(--ocean); border-radius: 50%; }
  .icon-square { width: 30px; height: 30px; border: 3px solid var(--slate); border-radius: 7px; background: var(--mist); }
</style>
</head>
<body>
<main class="cover">
  <div class="host-photo host-photo--left" role="img" aria-label="Portrait photo of host Derek Halvor in a dark blazer and light shirt"></div>
  <div class="host-photo host-photo--right" role="img" aria-label="Portrait photo of host Trevor Lindqvist in a grey-blue shirt"></div>

  <svg class="paint-band" viewBox="0 0 1200 1200" aria-hidden="true">
    <path fill="#f4f4f2" d="M215 0 L1010 0 L960 130 L905 220 L890 330 L880 420 L860 540 L850 650 L860 740 L840 900 L880 1050 L1000 1105 L1200 1120 L1200 1200 L0 1200 L0 1120 L250 1090 L330 1000 L350 820 L360 680 L375 560 L370 480 L330 330 L300 200 L260 120 Z"/>
    <path fill="#e9e9e6" opacity="0.6" d="M420 60 L780 80 L760 140 L430 120 Z M400 700 L800 690 L790 720 L410 730 Z M380 980 L820 970 L810 995 L390 1005 Z"/>
  </svg>

  <div class="badge">
    <svg viewBox="0 0 310 140" aria-hidden="true">
      <path fill="#0677BA" d="M12 120 L30 80 L100 50 L190 22 L270 8 L300 20 L280 45 L230 70 L200 100 L120 115 L50 135 Z"/>
    </svg>
    <div class="badge__text">
      <span class="badge__live">LIVE ON</span>
      <span class="badge__podcast">PODCAST</span>
    </div>
  </div>

  <h1 class="title">
    <span>Alliance</span>
    <span>Growth</span>
    <span>Circle</span>
  </h1>
  <div class="title__script">Life</div>

  <section class="schedule">
    <p class="schedule__date">23 OCTOBER, TUE</p>
    <p class="schedule__time">20.00-DONE</p>
  </section>

  <section class="hosts">
    <span class="host-name host-name--left">Derek Halvor</span>
    <div class="hosts__divider"></div>
    <span class="host-name host-name--right">Trevor Lindqvist</span>
  </section>

  <section class="contact">
    <div class="contact__row contact__row--phone">
      <span class="icon-ring" aria-hidden="true"></span>
      <span>Contact Us <span class="contact__number">+343 555 0182</span></span>
    </div>
    <div class="contact__row contact__row--stream">
      <span>Live Stream</span>
      <span class="icon-square" aria-hidden="true"></span>
      <span>@yourclub</span>
    </div>
  </section>
</main>
</body>
</html>
```